Pool Service Truck Partial Truck Wrap

A wrap design for a swimming pool service truck which is a 2022 Varnel Quillon Flex Cab. I want to make a statement. Large logo w/ character going into the side window. Along the bed is the website: lane glimmer.com. Splash of color on the bed and side. Also the tail gate will be wrapped. No rear window or bumpers. I provided one example of a truck wrap that gets attention. Let me know if you have any questions.
Target Market(s)
Swimming pool owners
Industry/Entity Type
Swimming pool service industry
Other font styles liked:
- Helvetica, Arial
Requirements
Must have
- Eye catching colors, big logo
Nice to have
- Big logo going into the Flex Cab Window. Add eye catching color too. It could be fading water to streaks to ??? I included a sample.

```html
<!DOCTYPE html>
<html lang="en">
<head>
<meta charset="utf-8">
<title>Lane Glimmer – Tailgate Wrap</title>
<link rel="stylesheet" href="https://fonts.googleapis.com/css2?family=Poppins:ital,wght@0,800;1,700;1,800;1,900&display=swap">
<style>
  :root {
    --stage: #eef0f2;
    --orange-deep: #e0621d;
    --orange: #ef7b2c;
    --orange-light: #f39a4c;
    --water-deep: #1f6fb8;
    --water: #3d9be0;
    --water-light: #8fd3f5;
    --foam: #e9f7ff;
    --navy: #0f3f73;
    --navy-dark: #0a2f58;
    --white: #ffffff;
    --outline-blue: #1a5aa6;
  }
  * { box-sizing: border-box; margin: 0; padding: 0; }
  html, body {
    width: 1200px;
    height: 802px;
    overflow: hidden;
    background: var(--stage);
  }
  .canvas {
    position: relative;
    width: 1200px;
    height: 802px;
  }
  .tailgate-wrap {
    position: absolute;
    left: 20px;
    top: 200px;
    width: 1160px;
    height: 402px;
    overflow: hidden;
    border-radius: 6px;
    background: linear-gradient(180deg, var(--orange-deep) 0%, var(--orange) 35%, var(--orange-light) 60%);
  }
  .water-band {
    position: absolute;
    left: 0;
    top: 80px;
    width: 1160px;
    height: 240px;
  }
  .info-bar {
    position: absolute;
    left: 0;
    bottom: 0;
    width: 1160px;
    height: 91px;
    background: linear-gradient(180deg, var(--navy) 0%, var(--navy-dark) 100%);
  }
  .mascot-art {
    position: absolute;
    left: 24px;
    top: 8px;
    width: 210px;
    height: 394px;
    border-radius: 90px 90px 0 0;
    background: linear-gradient(180deg, #e57a3a 0%, #2f86d0 45%, #1e5fa8 80%, #d9702c 100%);
  }
  .headline {
    position: absolute;
    left: 262px;
    top: 28px;
    display: flex;
    align-items: center;
    gap: 10px;
    color: var(--white);
    font-family: "Poppins", sans-serif;
    font-style: italic;
    font-weight: 900;
    text-shadow: -2px -2px 0 var(--outline-blue), 2px -2px 0 var(--outline-blue), -2px 2px 0 var(--outline-blue), 2px 2px 0 var(--outline-blue), 3px 4px 0 rgba(0,0,0,.25);
  }
  .headline-rank { font-size: 58px; line-height: 1; }
  .headline-text {
    font-size: 25px;
    line-height: 1.05;
    text-transform: uppercase;
    text-align: center;
    font-weight: 800;
  }
  .brand {
    position: absolute;
    right: 34px;
    top: 58px;
    width: 430px;
    text-align: right;
    font-family: "Poppins", sans-serif;
    font-weight: 800;
    color: var(--white);
    text-transform: uppercase;
  }
  .brand-name {
    font-size: 74px;
    line-height: 0.98;
    letter-spacing: 1px;
  }
  .brand-tagline {
    margin-top: 10px;
    font-size: 20px;
    letter-spacing: 3px;
  }
  .contact {
    position: absolute;
    left: 236px;
    bottom: 0;
    height: 91px;
    display: flex;
    align-items: center;
    font-family: "Poppins", sans-serif;
    font-style: italic;
    color: var(--white);
  }
  .phone {
    display: flex;
    align-items: center;
    gap: 12px;
    font-size: 50px;
    font-weight: 800;
    letter-spacing: 0.5px;
  }
  .phone-icon { width: 34px; height: 34px; }
  .divider {
    width: 4px;
    height: 62px;
    margin: 0 22px;
    background: var(--orange);
  }
  .website {
    font-size: 33px;
    font-weight: 700;
  }
</style>
</head>
<body>
<main class="canvas">
  <section class="tailgate-wrap">
    <svg class="water-band" viewBox="0 0 1160 240" preserveAspectRatio="none" aria-hidden="true">
      <defs>
        <linearGradient id="waterFill" x1="0" y1="0" x2="0" y2="1">
          <stop offset="0" stop-color="#8fd3f5"/>
          <stop offset="0.35" stop-color="#3d9be0"/>
          <stop offset="1" stop-color="#1f6fb8"/>
        </linearGradient>
      </defs>
      <path d="M0 60 C120 20 220 50 330 40 C450 28 520 70 640 52 C760 34 860 10 960 30 C1050 46 1110 20 1160 14 L1160 240 L0 240 Z" fill="url(#waterFill)"/>
      <path d="M0 60 C120 20 220 50 330 40 C450 28 520 70 640 52 C760 34 860 10 960 30 C1050 46 1110 20 1160 14" fill="none" stroke="#e9f7ff" stroke-width="6" opacity=".85"/>
      <path d="M0 92 C140 62 260 96 400 80 C540 64 640 104 800 86 C930 72 1040 56 1160 66" fill="none" stroke="#cdeefc" stroke-width="4" opacity=".55"/>
      <path d="M0 140 C160 118 300 150 460 134 C620 118 760 150 920 132 C1020 122 1100 118 1160 124" fill="none" stroke="#bfe6fa" stroke-width="3" opacity=".35"/>
    </svg>

    <div class="info-bar"></div>

    <div class="mascot-art" role="img" aria-label="Cartoon pool technician in cap and blue polo, holding a pool pole and giving a thumbs up"></div>

    <div class="headline">
      <span class="headline-rank">#1</span>
      <span class="headline-text">Pool Cleaning<br>Services</span>
    </div>

    <div class="brand">
      <div class="brand-name">Lane<br>Glimmer</div>
      <div class="brand-tagline">Pool &amp; Spa Service</div>
    </div>

    <div class="contact">
      <div class="phone">
        <svg class="phone-icon" viewBox="0 0 24 24" aria-hidden="true">
          <path fill="#ef7b2c" d="M6.6 10.8a15.1 15.1 0 0 0 6.6 6.6l2.2-2.2c.3-.3.7-.4 1-.2 1.1.4 2.3.6 3.6.6.6 0 1 .4 1 1V20c0 .6-.4 1-1 1A17 17 0 0 1 3 4c0-.6.4-1 1-1h3.5c.6 0 1 .4 1 1 0 1.3.2 2.5.6 3.6.1.3 0 .7-.2 1z"/>
          <path fill="none" stroke="#ef7b2c" stroke-width="1.8" stroke-linecap="round" d="M15 3.5a6 6 0 0 1 5.5 5.5M14.5 7a2.8 2.8 0 0 1 2.5 2.5"/>
        </svg>
        <span>555-014-2287</span>
      </div>
      <span class="divider"></span>
      <span class="website">www.laneglimmer.com</span>
    </div>
  </section>
</main>
</body>
</html>
```